Waterjet Cutting Business requires an up to date website

We currently have a website which is outdated and in need of modernization.
We are only looking for a simple website with around 4 pages: Home, Contact Us, Materials, Gallery.
We have some pictures and a logo which can be used.
Our primary business is profile cutting of materials to customers specifications using high-pressure water with abrasive.
We are looking for creative ideas and are open to suggestions!
http://brightfordcutworks.com/index.asp?pid=1
Update:
Cut quality picture (uploaded)
Map
Comparison to other profile cutting methods such as plasma/laser
Single page style without continuous scrolling
"We can cut virtually any material from any drawing whether it be a Full 3D cad models to hand sketched "
Target Market(s)
Film Industry, Prototype, Engineering, Architect, Artisits, one off designs
Industry/Entity Type
Engineering
Number of Pages Required
1 page
Font styles to use
Look and feel

```html
<!DOCTYPE html>
<html lang="en">
<head>
<meta charset="utf-8">
<title>Contact Us – Brightford Cutworks</title>
<link href="https://fonts.googleapis.com/css2?family=Montserrat:wght@500;700;800&family=Lato:wght@400;700&display=swap" rel="stylesheet">
<style>
  :root {
    --ink: #000000;
    --paper: #ffffff;
    --photo-deep: #0b1026;
    --photo-blue: #1f3a8a;
    --photo-violet: #3a2a6e;
    --photo-magenta: #8a2a5c;
    --nav-shade: rgba(0, 0, 0, 0.5);
  }
  * { box-sizing: border-box; margin: 0; padding: 0; }
  html, body {
    width: 1200px; height: 675px; overflow: hidden;
    background: var(--ink);
  }
  .page {
    position: relative; width: 1200px; height: 675px;
    background: var(--ink); color: var(--paper);
    font-family: "Montserrat", Arial, sans-serif;
    overflow: hidden;
  }
  .hero-photo { position: absolute; inset: 0; width: 1200px; height: 675px; }

  .brand {
    position: absolute; left: 178px; top: 40px;
    display: flex; align-items: center; gap: 10px;
    font-weight: 800; font-size: 21px; letter-spacing: 0.5px;
    text-transform: uppercase;
  }
  .brand-dot { width: 12px; height: 12px; background: var(--paper); border-radius: 50%; }

  .main-nav {
    position: absolute; top: 47px; left: 597px;
    display: flex; align-items: center;
    font-family: "Lato", Arial, sans-serif; font-size: 15.5px; letter-spacing: 0.3px;
  }
  .main-nav a { color: var(--paper); text-decoration: none; margin-right: 27px; }
  .main-nav .nav-cta {
    margin-left: 13px; margin-right: 0;
    background: var(--paper); color: var(--ink);
    width: 131px; height: 31px; border-radius: 5px;
    display: flex; align-items: center; justify-content: center;
  }

  .page-title {
    position: absolute; left: 176px; top: 136px;
    font-weight: 800; font-size: 35px; letter-spacing: 1.5px;
  }

  .contact-item { position: absolute; left: 176px; display: flex; }
  .contact-icon { width: 70px; display: flex; justify-content: center; }
  .contact-text { font-size: 13.5px; font-weight: 500; line-height: 21px; letter-spacing: 0.5px; margin-left: 3px; }
  .contact-address { top: 229px; }
  .contact-phone { top: 389px; }
  .contact-email { top: 515px; }

  .enquiry-form { position: absolute; left: 534px; top: 214px; width: 416px; }
  .field {
    position: absolute; border: 1px solid var(--paper);
    font-family: "Lato", Arial, sans-serif; font-weight: 700; font-size: 13px;
    padding: 14px 0 0 8px; color: var(--paper);
  }
  .field-name { left: 0; top: 0; width: 203px; height: 42px; }
  .field-email { left: 214px; top: 0; width: 202px; height: 42px; }
  .field-phone { left: 0; top: 53px; width: 416px; height: 42px; }
  .field-message { left: 0; top: 106px; width: 416px; height: 265px; }
</style>
</head>
<body>
<div class="page">
  <svg class="hero-photo" viewBox="0 0 1200 675" role="img" aria-label="Close-up photo of a waterjet cutting head over a slatted metal bed, lit in deep blue and magenta">
    <defs>
      <linearGradient id="photoTone" x1="0" y1="1" x2="1" y2="0">
        <stop offset="0" stop-color="var(--photo-deep)"/>
        <stop offset="0.45" stop-color="var(--photo-blue)"/>
        <stop offset="0.75" stop-color="var(--photo-violet)"/>
        <stop offset="1" stop-color="var(--photo-magenta)"/>
      </linearGradient>
      <clipPath id="waveEdge">
        <path d="M654 0 C660 60 640 120 590 180 C520 240 450 300 448 400 C446 480 480 560 518 675 L1200 675 L1200 0 Z"/>
      </clipPath>
    </defs>
    <g clip-path="url(#waveEdge)">
      <rect width="1200" height="675" fill="url(#photoTone)"/>
      <rect width="1200" height="114" fill="var(--nav-shade)"/>
    </g>
  </svg>

  <header>
    <div class="brand"><span class="brand-dot"></span>Brightford Cutworks</div>
    <nav class="main-nav">
      <a href="#">HOME</a>
      <a href="#">MATERIALS</a>
      <a href="#">GALLERY</a>
      <a href="#" class="nav-cta">CONTACT</a>
    </nav>
  </header>

  <h1 class="page-title">Contact Us</h1>

  <div class="contact-item contact-address">
    <div class="contact-icon">
      <svg width="34" height="50" viewBox="0 0 34 50" fill="none" stroke="#fff" stroke-width="2">
        <path d="M17 48 C10 36 2 27 2 17 A15 15 0 0 1 32 17 C32 27 24 36 17 48 Z"/>
        <circle cx="17" cy="17" r="5.5"/>
      </svg>
    </div>
    <p class="contact-text">Address<br>Unit 7, Ridgeway 2, Alder<br>Road, Fenmoor Trade<br>Park, Ashcombe,<br>Wessex, AC4 9TL</p>
  </div>

  <div class="contact-item contact-phone">
    <div class="contact-icon">
      <svg width="50" height="50" viewBox="0 0 50 50" fill="none" stroke="#fff" stroke-width="2" stroke-linejoin="round">
        <path d="M10 3 L17 11 C18.5 13 18 15 16 17 L13 20 C16 28 22 34 30 37 L33 34 C35 32 37 31.5 39 33 L47 40 C48 42 47.5 44 46 45.5 L43 48 C38 50 30 47 21 39 C11 30 2 19 2 11 C2 8 4 5 6 3.5 C7.5 2 9 2 10 3 Z"/>
      </svg>
    </div>
    <p class="contact-text">Telephone<br>01632 960418</p>
  </div>

  <div class="contact-item contact-email">
    <div class="contact-icon">
      <svg width="62" height="50" viewBox="0 0 62 50" fill="none" stroke="#fff" stroke-width="2" stroke-linejoin="round">
        <path d="M38 42 H2 V2 H60 V24"/>
        <path d="M2 2 L31 26 L60 2"/>
        <path d="M2 42 L22 19"/>
        <path d="M54 24 L60 30 L44 46 L36 48 L38 40 Z"/>
        <path d="M50 28 L56 34"/>
      </svg>
    </div>
    <p class="contact-text">Email<br>info@brightfordcutworks.com</p>
  </div>

  <form class="enquiry-form">
    <div class="field field-name">Name</div>
    <div class="field field-email">Email</div>
    <div class="field field-phone">Phone</div>
    <div class="field field-message">Message</div>
  </form>
</div>
</body>
</html>
```